Yacht, Boats, Watersports company needs a redesign of business card

Hello Designers!
We are a Boat dealership company that sells fun in the water, we sell boats, Yachts, Kayaks and also yacht WaterSport toys. We are looking to redesign our business cards in to something a little bit more sophisticated. in a way that we can make better use of our company colors. I'm attaching a zipped file containing the company 3 sets of company logo which one is an horizontal another one is a vertical and also a chromed 3d logo. Also is included two set of business cards that we use and also some designs that i think it's interesting. We use PMS 2026c Orange and PMS 7687C Blue. I would like to see at least two different options with the orange as accent and also using blue as an accent color. It's really important for the business cards to have a font option and size that is legible to most people. Our current website is wwww.corvellamarine.com. Please visit if you want to have a better feeling of the Boat dealership
You can send Single sided or double side options. We are now using single sided but we may be open for a double side option if we really like the design.
Target Market(s)
Marine, boat sales, yacht sales, water toys sales/
Contact Information for Business Card
Name: Dale Pritchett
Address: 718 West Halden Lane,
Dania Beach, FL 33019
Phone: 954-382-7146
Fax: 954:382-7139
Cell: 954-451-8320
Email: 212@corvellamarine.com
Website: corvellamarine.com
Requirements
Must have
- the current information of the business card provided.
logo
use the PMS Colors
Nice to have
- a touch of elegance and sophistication but simple
Should not have
- should not have any typography that is hard to read, the card should be simple but yet sophisticated.

```html
<!DOCTYPE html>
<html lang="en">
<head>
<meta charset="utf-8">
<title>Corvella Marine – Business Card</title>
<link href="https://fonts.googleapis.com/css2?family=Montserrat:wght@700&family=Roboto:wght@400&display=swap" rel="stylesheet">
<style>
  :root {
    --brand-blue: #24457e;
    --brand-orange: #f04e23;
    --paper: #ffffff;
    --stage: #ffffff;
  }
  * { margin: 0; padding: 0; box-sizing: border-box; }
  html, body { width: 1200px; height: 525px; overflow: hidden; background: var(--stage); }
  .canvas { position: relative; width: 1200px; height: 525px; }

  .card {
    position: absolute;
    width: 500px;
    height: 286px;
    overflow: hidden;
  }
  .card--back {
    left: 79px; top: 114px;
    background: var(--brand-blue);
    box-shadow: -4px 5px 6px rgba(0,0,0,.45);
  }
  .card--front {
    left: 627px; top: 116px;
    background: var(--paper);
    box-shadow: 0 1px 4px rgba(0,0,0,.35);
  }

  /* back: centred wordmark */
  .back-mark {
    position: absolute; left: 0; top: 0; width: 100%; height: 100%;
    display: flex; align-items: center; justify-content: center; gap: 12px;
  }
  .back-mark__dot {
    width: 22px; height: 22px; border: 4px solid var(--paper); border-radius: 50%;
  }
  .back-mark__name {
    font-family: "Montserrat", sans-serif; font-weight: 700;
    font-size: 22px; letter-spacing: 3px; color: var(--paper);
  }

  /* front: wordmark */
  .front-mark {
    position: absolute; left: 32px; top: 62px;
    display: flex; align-items: center; gap: 16px;
  }
  .front-mark__dot {
    width: 28px; height: 28px; border-radius: 50%; background: var(--brand-orange);
  }
  .front-mark__name {
    font-family: "Montserrat", sans-serif; font-weight: 700;
    font-size: 22px; letter-spacing: 4px; color: var(--brand-blue);
  }

  .person {
    position: absolute; right: 32px; top: 146px; text-align: right;
    font-family: "Montserrat", sans-serif; font-weight: 700;
  }
  .person__name { font-size: 15.5px; color: var(--brand-orange); line-height: 18px; }
  .person__title { font-size: 11px; color: var(--brand-blue); line-height: 13px; }

  .divider {
    position: absolute; left: 31px; top: 180px; width: 437px; height: 1px;
    background: var(--brand-orange);
  }

  .contacts {
    position: absolute; left: 31px; top: 192px; list-style: none;
    font-family: "Roboto", sans-serif; font-size: 13px; color: var(--brand-blue);
  }
  .contacts li { display: flex; align-items: center; height: 17px; }
  .contacts svg { width: 12px; height: 12px; margin-right: 6px; flex: none; }

  .address {
    position: absolute; right: 32px; top: 224px; text-align: right;
    font-family: "Roboto", sans-serif; font-size: 13px; line-height: 19px;
    font-style: normal; color: var(--brand-blue);
  }

  .web-band {
    position: absolute; left: 0; bottom: 0; width: 100%; height: 20px;
  }
  .web-band svg { position: absolute; left: 0; top: 0; }
  .web-band__url {
    position: absolute; right: 32px; top: 2px;
    font-family: "Roboto", sans-serif; font-size: 12.5px; color: var(--paper);
  }
</style>
</head>
<body>
<div class="canvas">

  <section class="card card--back" aria-label="Card back">
    <div class="back-mark">
      <span class="back-mark__dot"></span>
      <span class="back-mark__name">CORVELLA MARINE</span>
    </div>
  </section>

  <section class="card card--front" aria-label="Card front">
    <div class="front-mark">
      <span class="front-mark__dot"></span>
      <span class="front-mark__name">CORVELLA MARINE</span>
    </div>

    <div class="person">
      <p class="person__name">DALE PRITCHETT</p>
      <p class="person__title">OWNER CEO</p>
    </div>

    <div class="divider"></div>

    <ul class="contacts">
      <li>
        <svg viewBox="0 0 12 12" aria-hidden="true"><rect x="2.5" y="0.8" width="7" height="10.4" rx="1.4" fill="none" stroke="var(--brand-orange)" stroke-width="1.4"/><circle cx="6" cy="9.2" r="0.8" fill="var(--brand-orange)"/></svg>
        954-451-8320
      </li>
      <li>
        <svg viewBox="0 0 12 12" aria-hidden="true"><path d="M2.4 0.8 L4.4 0.8 L5.2 3.4 L3.9 4.5 Q5 7 7.5 8.1 L8.6 6.8 L11.2 7.6 L11.2 9.6 Q11 11.2 9.4 11.2 Q1 10.5 0.8 2.6 Q0.8 0.9 2.4 0.8 Z" fill="var(--brand-orange)"/></svg>
        954-382-7146
      </li>
      <li>
        <svg viewBox="0 0 12 12" aria-hidden="true"><path d="M2.4 0.8 L4.4 0.8 L5.2 3.4 L3.9 4.5 Q5 7 7.5 8.1 L8.6 6.8 L11.2 7.6 L11.2 9.6 Q11 11.2 9.4 11.2 Q1 10.5 0.8 2.6 Q0.8 0.9 2.4 0.8 Z" fill="var(--brand-orange)"/></svg>
        561-274-9053
      </li>
      <li>
        <svg viewBox="0 0 12 12" aria-hidden="true"><rect x="0.5" y="2.5" width="11" height="7.5" fill="var(--brand-orange)"/><path d="M0.8 2.8 L6 6.8 L11.2 2.8" fill="none" stroke="var(--paper)" stroke-width="1"/></svg>
        212@corvellamarine.com
      </li>
    </ul>

    <address class="address">
      718 West Halden Lane,<br>
      Marlow Cove, FL 33019
    </address>

    <div class="web-band">
      <svg width="500" height="20" aria-hidden="true"><polygon points="264,0 500,0 500,20 250,20" fill="var(--brand-orange)"/></svg>
      <span class="web-band__url">www.corvellamarine.com</span>
    </div>
  </section>

</div>
</body>
</html>
```